Cat sitting business Web Design Project ***

I have a cat sitting business where I either take care of cats in their home or board them in mine

I need a website which offers my services, my rates, about me, FAQ's, Hours of operation and service areas covered, testimonials, contact info, newsletter sign up, gallery of photos and the ability for me to go in and update when needed.

Coding

Coded - Design and coding required

Number of Pages Required

5+ page

```html
<!DOCTYPE html>
<html lang="en">
<head>
<meta charset="utf-8">
<title>Velvet Paws Cat Sitting</title>
<link rel="stylesheet" href="https://fonts.googleapis.com/css2?family=Montserrat:wght@500;700;800&family=Open+Sans:wght@400;600;700&family=Playball&family=Ubuntu:wght@500;700&display=swap">
<style>
:root{
  --brand:#a0463f;
  --brand-dark:#8a3a34;
  --green:#7cc143;
  --green-dark:#5fa22c;
  --pink:#f3d3d1;
  --ink:#333;
  --muted:#666;
  --card:#dcdcdc;
  --line:#222;
  --footer:#a0503f;
  --footer-bar:#4a4a4a;
}
*{box-sizing:border-box;margin:0;padding:0}
html,body{width:1200px;height:4971px;overflow:hidden}
body{position:relative;font-family:"Open Sans",Arial,sans-serif;color:var(--ink);background:#fff}
.abs{position:absolute}
.section{position:absolute;left:0;width:1200px}
.heading{position:absolute;left:0;width:1200px;text-align:center;font-family:"Ubuntu",Arial,sans-serif;font-weight:500;font-size:34px;color:var(--green)}
.heading svg{width:36px;height:36px;vertical-align:-4px;margin-right:8px;fill:var(--brand)}
.heading.light svg{fill:#fff}
.rule{position:absolute;left:567px;width:66px;height:3px;background:#333}
.read-more{position:absolute;height:20px;padding:0 26px 0 10px;border-radius:10px;background:var(--brand);color:#fff;font-size:9px;font-weight:700;line-height:20px;letter-spacing:.5px}
.read-more::after{content:"";position:absolute;right:3px;top:3px;width:14px;height:14px;border-radius:50%;background:var(--green)}

/* header */
.logo{left:150px;top:38px;display:flex;align-items:center;gap:10px;font-family:"Open Sans",sans-serif;font-weight:600;font-size:20px;color:var(--brand)}
.logo i{width:26px;height:26px;border-radius:50%;background:var(--green);display:block}
.call{left:770px;top:44px;font-family:"Open Sans",sans-serif;font-weight:700;color:#e0a83a;font-size:20px;line-height:24px}
.call b{display:block;color:var(--brand);font-size:20px}
.follow{left:977px;top:36px;font-weight:700;font-size:17px;color:var(--green)}
.follow span{display:flex;gap:4px;margin-top:6px}
.follow span i{width:21px;height:21px;background:#3c6fb2;display:block}
.nav{top:129px;height:41px;background:var(--brand)}
.nav a{position:absolute;top:0;line-height:41px;color:#fff;font-family:"Open Sans",sans-serif;font-weight:600;font-size:19px;text-decoration:none;letter-spacing:.5px}
.nav .sep{position:absolute;top:6px;width:1px;height:29px;background:rgba(255,255,255,.35)}

/* hero */
.hero{top:170px;height:780px;background:linear-gradient(100deg,#2f3a48 0%,#545c66 35%,#6f6862 60%,#463f3a 100%)}
.hero-text{position:absolute;left:0;width:1200px;text-align:center}
.script{top:345px;font-family:"Playball",cursive;font-size:86px;color:var(--green);line-height:1}
.caps{top:445px;font-family:"Montserrat",sans-serif;font-weight:800;font-size:42px;color:var(--green);letter-spacing:1px}
.sub{top:490px;font-family:"Montserrat",sans-serif;font-weight:700;font-size:34px;color:#fff}
.cta{left:486px;top:553px;width:228px;height:43px;background:var(--brand);color:#fff;font-weight:600;font-size:15px;line-height:43px;text-align:center;border-radius:3px}
.cta svg{width:18px;height:18px;fill:#fff;vertical-align:-3px;margin-right:6px}

/* about */
.about{top:950px;height:559px}
.about-photo{left:137px;top:184px;width:434px;height:296px;background:linear-gradient(135deg,#c9b79e,#7a6a5a 55%,#3a3330)}
.about-copy{left:608px;top:187px;width:464px;font-size:12.5px;line-height:15px;color:#444;text-align:justify}
.about-copy p{margin-bottom:11px}
.about-copy p.bold{font-weight:600;color:#222}

/* services */
.services{top:1509px;height:613px;background:var(--pink)}
.svc{position:absolute;width:260px;text-align:center}
.svc .photo{width:196px;height:196px;margin:0 auto;border-radius:50%;border:5px solid var(--brand)}
.svc h3{margin-top:30px;font-family:"Montserrat",sans-serif;font-weight:500;font-size:19px;color:var(--brand)}
.svc svg{width:24px;height:24px;fill:var(--green);margin:10px 0 6px}
.svc p{font-size:12.5px;line-height:15px;color:#333}
.arrow{position:absolute;fill:none;stroke:#999;stroke-width:2}

/* faq */
.faq{top:2122px;height:560px}
.faq-item{position:absolute;left:141px;width:926px;font-family:"Open Sans",sans-serif}
.faq-item h4{font-weight:600;font-size:19px;color:var(--brand)}
.faq-item .toggle{position:absolute;right:0;top:-4px;font-size:28px;color:#222;font-weight:400}
.faq-item p{margin-top:6px;width:640px;font-size:12.5px;line-height:15px;color:#333}
.faq-item.closed{border-bottom:3px solid var(--line);padding-bottom:15px}

/* rates */
.rates{top:2682px;height:669px;background:var(--green)}
.rates .heading{color:#fff}
.rates .rule{background:#fff}
.plan{position:absolute;width:197px}
.plan-tab{height:55px;background:var(--brand);border-radius:14px 14px 0 0;color:#fff;text-align:center;font-family:"Ubuntu",sans-serif;font-weight:500;font-size:29px;line-height:50px}
.plan-body{margin-top:-8px;background:var(--card);border-radius:14px;padding:22px 0 18px;text-align:center}
.price{font-family:"Ubuntu",sans-serif;font-weight:700;font-size:46px;color:var(--brand);line-height:1}
.price sup{font-size:22px}
.plan-note{margin-top:8px;font-weight:700;font-size:14px;line-height:15px;color:var(--brand)}
.plan ul{list-style:none;text-align:left;padding-left:22px;margin-top:6px}
.plan li{font-size:15px;line-height:21px;color:#222}
.plan li svg{width:12px;height:12px;stroke:var(--brand);stroke-width:3;fill:none;margin-right:8px;vertical-align:-1px}
.select{display:inline-block;margin-top:12px;height:22px;padding:0 28px 0 16px;border-radius:11px;background:var(--green);color:#fff;font-weight:700;font-size:12px;line-height:22px;position:relative}
.select::after{content:"";position:absolute;right:5px;top:4px;width:14px;height:14px;border-radius:50%;background:#fff}

/* testimonials */
.testimonials{top:3351px;height:440px}
.quote{position:absolute;width:361px;height:151px;border:2px solid #9a9a9a;padding:34px 24px 0}
.quote .mark{position:absolute;left:24px;top:-14px;font-family:"Ubuntu",sans-serif;font-weight:700;font-size:54px;line-height:1;color:var(--brand);background:#fff;padding:0 4px}
.quote h5{font-weight:600;font-size:14px;color:var(--green)}
.quote p{margin-top:6px;font-size:12.5px;line-height:17px;color:#777}
.quote::after{content:"";position:absolute;left:30px;bottom:-11px;width:18px;height:18px;background:#fff;border-right:2px solid #9a9a9a;border-bottom:2px solid #9a9a9a;transform:rotate(45deg)}
.who{position:absolute;font-weight:700;font-size:15px;color:var(--green)}
.who span{display:block;font-weight:400;font-size:13px;color:#888}

/* newsletter */
.newsletter{top:3795px;height:73px;background:var(--brand)}
.mail-icon{left:220px;top:12px;width:48px;height:48px;border-radius:50%;background:#fff}
.mail-icon i{position:absolute;left:6px;top:6px;width:36px;height:36px;border-radius:50%;background:var(--green)}
.mail-icon svg{position:absolute;left:14px;top:16px;width:20px;height:16px;fill:none;stroke:#fff;stroke-width:2}
.newsletter h6{position:absolute;left:311px;top:20px;font-family:"Open Sans",sans-serif;font-weight:400;font-size:27px;color:#fff}
.nl-input{left:611px;top:25px;width:354px;height:29px;background:#fff;font-size:12px;line-height:29px;padding-left:25px;color:#333}
.nl-btn{left:965px;top:25px;width:117px;height:29px;background:var(--green);color:#fff;font-size:13px;line-height:29px;text-align:center}

/* gallery */
.gallery{top:3868px;height:733px;background:linear-gradient(180deg,#f7f6f5,#efeeec)}
.tile{position:absolute;width:216px;height:204px;border:4px solid #fff;box-shadow:0 1px 4px rgba(0,0,0,.15)}

/* footer */
.footer{top:4601px;height:309px;background:var(--footer);color:#fff}
.footer h6{position:absolute;top:80px;font-family:"Open Sans",sans-serif;font-weight:700;font-size:17px;letter-spacing:.5px}
.footer ul{position:absolute;top:126px;list-style:none;font-size:13.5px;line-height:18px}
.footer ul li::before{content:"";display:inline-block;border-left:6px solid #fff;border-top:4px solid transparent;border-bottom:4px solid transparent;margin-right:12px}
.footer .col{position:absolute;top:125px;font-size:13.5px;line-height:18px}
.footer .col p{margin-bottom:18px}
.f-input{position:absolute;left:836px;width:218px;height:30px;background:#fff;color:#333;font-size:11px;line-height:30px;padding-left:14px}
.f-btn{position:absolute;left:842px;top:210px;width:112px;height:20px;border-radius:10px;background:var(--green);font-size:10px;font-weight:700;line-height:20px;padding-left:14px}
.copy{top:4910px;height:61px;background:var(--footer-bar);color:#ddd;font-size:12px;text-align:center;line-height:61px}
</style>
</head>
<body>
<svg width="0" height="0" style="position:absolute">
  <symbol id="paw" viewBox="0 0 24 24">
    <ellipse cx="6" cy="8" rx="2.4" ry="3.2"/><ellipse cx="10.2" cy="4.6" rx="2.4" ry="3.2"/>
    <ellipse cx="15" cy="5.2" rx="2.4" ry="3.2"/><ellipse cx="18.6" cy="9.6" rx="2.3" ry="3"/>
    <path d="M12 11c-3 0-6.5 4-6.5 7 0 2.5 2.5 3 4 2.4 1.4-.5 3.6-.5 5 0 1.5.6 4 .1 4-2.4 0-3-3.5-7-6.5-7z"/>
  </symbol>
  <symbol id="tick" viewBox="0 0 12 12"><path d="M1.5 6.5l3 3 6-7"/></symbol>
</svg>

<!-- header -->
<header class="section" style="top:0;height:129px">
  <div class="abs logo"><i></i>Velvet Paws Cat Sitting</div>
  <div class="abs call">Call Us<b>012-555-0147</b></div>
  <div class="abs follow">Follow Us<span><i></i><i></i><i></i><i></i></span></div>
</header>
<nav class="section nav">
  <a style="left:141px">HOME</a><span class="sep" style="left:232px"></span>
  <a style="left:260px">ABOUT</a><span class="sep" style="left:355px"></span>
  <a style="left:386px">SERVICES</a><span class="sep" style="left:505px"></span>
  <a style="left:532px">GALLERY</a><span class="sep" style="left:655px"></span>
  <a style="left:683px">PRICING</a><span class="sep" style="left:795px"></span>
  <a style="left:824px">FAQ</a><span class="sep" style="left:915px"></span>
  <a style="left:941px">CONTACT US</a>
</nav>

<!-- hero -->
<section class="section hero" role="img" aria-label="Photo of a veterinarian gently examining a grey and white cat">
  <div class="hero-text script">Philosohorum</div>
  <div class="hero-text caps">PHILOSOPHI AUTEM IN SUIS</div>
  <div class="hero-text sub">Lectulis plerumque moriuntu rutem</div>
  <div class="abs cta"><svg><use href="#paw"/></svg>Make An Appointment</div>
</section>

<!-- about -->
<section class="section about">
  <h2 class="heading" style="top:58px"><svg><use href="#paw"/></svg>About Us</h2>
  <div class="rule" style="top:116px"></div>
  <div class="abs about-photo" role="img" aria-label="Photo of the cat sitter holding a white cat on a sofa"></div>
  <div class="abs about-copy">
    <p>Verum tamen cum de rebus grandioribus dicas, ipsae res verba rapiunt; Hoc non est positum in nostra actione. Quod ea non occurrentia fingunt, vincunt Aristonem; Haec para/doca illi, nos admirabilia dicamus. Et quidem, inquit, vehementer errat; Quarum ambarum rerum cum medicinam poli-cetur, luxuriae licentiam</p>
    <p>pollicetur. Laelius clamores sofôw ille so lebat Edere compellans gumias ex ordine nostros.Verum tamen cum de rebus grandioribus dicas, ipsae res verba rapiunt; Hoc non est positum in nostra actione. Quod ea non occur-rentia fingunt, vincunt Aristonem; Haec para/doca illi, nos admirabilia dicamus. Et quidem, inquit, vehementer errat; Quarum ambarum</p>
    <p class="bold">nostra actione. Quod ea non occurrentia fingunt, vincunt Aristonem; Haec para/doca illi, nos admirabilia dicamus. Et quidem, inquit, vehe-menter errat; Quarum ambarum</p>
  </div>
  <div class="read-more" style="left:610px;top:461px">READ MORE</div>
</section>

<!-- services -->
<section class="section services">
  <h2 class="heading" style="top:60px"><svg><use href="#paw"/></svg>Our Services</h2>
  <div class="rule" style="top:124px"></div>
  <svg class="arrow" style="left:80px;top:246px" width="24" height="50"><path d="M20 2L4 25l16 23"/></svg>
  <svg class="arrow" style="left:1108px;top:246px" width="24" height="50"><path d="M4 2l16 23L4 48"/></svg>
  <div class="svc" style="left:177px;top:168px">
    <div class="photo" role="img" aria-label="Photo of a cat paw being examined" style="background:linear-gradient(135deg,#d9d2c8,#8f8172)"></div>
    <h3>ARISTONEM</h3><svg><use href="#paw"/></svg>
    <p>Honesto quic quam honestius<br>nec turpi turpius. Tria genera bonorum<br>honestius nec turpi turpius.</p>
  </div>
  <div class="svc" style="left:480px;top:168px">
    <div class="photo" role="img" aria-label="Photo of a ginger and white cat at a vet check-up" style="background:linear-gradient(135deg,#b9d7d3,#e8c9a8)"></div>
    <h3>SRISTONEM</h3><svg><use href="#paw"/></svg>
    <p>Honesto quic quam honestius<br>nec turpi turpius. Tria genera bonorum<br>honestius nec turpi turpius.</p>
  </div>
  <div class="svc" style="left:775px;top:168px">
    <div class="photo" role="img" aria-label="Photo of a vet treating a dog in a clinic" style="background:linear-gradient(135deg,#a9c2d8,#d8c3a3)"></div>
    <h3>ERISTONEM</h3><svg><use href="#paw"/></svg>
    <p>Honesto quic quam honestius<br>nec turpi turpius. Tria genera bonorum<br>honestius nec turpi turpius.</p>
  </div>
  <div class="read-more" style="left:571px;top:556px">READ MORE</div>
</section>

<!-- faq -->
<section class="section faq">
  <h2 class="heading" style="top:60px"><svg><use href="#paw"/></svg>FAQ’S</h2>
  <div class="faq-item" style="top:128px">
    <h4>Est enim effectrix multarum et magnarum voluptatum</h4><span class="toggle">–</span>
    <p>Grandioribus dicas, ipsae res verba rapiunt; Hoc non est positum in nostra actione. Quod ea non occurrentia fingunt, vincunt Aristonem; Haec para/doca illi, nos admirabilia dicamus. Et quidem, inquit, vehementer errat; Quarum ambarum rerum .</p>
  </div>
  <div class="faq-item closed" style="top:250px"><h4>Est enim effectrix multarum et ?</h4><span class="toggle">+</span></div>
  <div class="faq-item closed" style="top:338px"><h4>Est enim effectrix multarum et ?</h4><span class="toggle">+</span></div>
  <div class="faq-item closed" style="top:427px"><h4>Est enim effectrix multarum et ?</h4><span class="toggle">+</span></div>
</section>

<!-- rates -->
<section class="section rates">
  <h2 class="heading light" style="top:80px"><svg><use href="#paw"/></svg><span style="color:#fff">My Rates</span></h2>
  <div class="rule" style="top:138px"></div>
  <div class="plan" style="left:222px;top:273px">
    <div class="plan-tab">Basic</div>
    <div class="plan-body">
      <div class="price">90<sup>$</sup></div>
      <div class="plan-note">Huic mori opti<br>sse propter desper</div>
      <ul><li><svg><use href="#tick"/></svg>Neque solum ea</li><li><svg><use href="#tick"/></svg>Communia, verum</li><li><svg><use href="#tick"/></svg>Etiam paria esse</li><li><svg><use href="#tick"/></svg>Dixerunt.</li><li><svg><use href="#tick"/></svg>Ruod si ita se</li><li><svg><use href="#tick"/></svg>Sabeat, non possit</li></ul>
      <span class="select">SELECT</span>
    </div>
  </div>
  <div class="plan" style="left:507px;top:163px">
    <div class="plan-tab">Standard</div>
    <div class="plan-body">
      <div class="price">90<sup>$</sup></div>
      <div class="plan-note">Huic mori opti<br>sse propter desper</div>
      <ul><li><svg><use href="#tick"/></svg>Neque solum ea</li><li><svg><use href="#tick"/></svg>Communia, verum</li><li><svg><use href="#tick"/></svg>Etiam paria esse</li><li><svg><use href="#tick"/></svg>Dixerunt.</li><li><svg><use href="#tick"/></svg>Ruod si ita se</li><li><svg><use href="#tick"/></svg>Sabeat, non possit</li></ul>
      <span class="select">SELECT</span>
    </div>
  </div>
  <div class="plan" style="left:800px;top:261px">
    <div class="plan-tab">Premium</div>
    <div class="plan-body">
      <div class="price">90<sup>$</sup></div>
      <div class="plan-note">Huic mori opti<br>sse propter desper</div>
      <ul><li><svg><use href="#tick"/></svg>Neque solum ea</li><li><svg><use href="#tick"/></svg>Communia, verum</li><li><svg><use href="#tick"/></svg>Etiam paria esse</li><li><svg><use href="#tick"/></svg>Dixerunt.</li><li><svg><use href="#tick"/></svg>Ruod si ita se</li><li><svg><use href="#tick"/></svg>Sabeat, non possit</li></ul>
      <span class="select">SELECT</span>
    </div>
  </div>
</section>

<!-- testimonials -->
<section class="section testimonials">
  <h2 class="heading" style="top:55px"><svg style="fill:var(--green)"><use href="#paw"/></svg><span style="color:var(--brand)">Testimonials</span></h2>
  <div class="rule" style="top:110px"></div>
  <svg class="arrow" style="left:142px;top:205px" width="22" height="46"><path d="M18 2L4 23l14 21"/></svg>
  <svg class="arrow" style="left:1038px;top:205px" width="22" height="46"><path d="M4 2l14 21L4 44"/></svg>
  <div class="quote" style="left:203px;top:163px"><span class="mark">“</span>
    <h5>Highly Professional Team</h5>
    <p>Abent ipsum dolor sit amet, consectetur adipi-scing elit. Quid autem habent admirationis, cum prope accesseris An hoc usque quaque, aliter in vita</p>
  </div>
  <div class="who" style="left:240px;top:340px">ZACHARY HOLM<span>Manager</span></div>
  <div class="quote" style="left:638px;top:163px"><span class="mark">“</span>
    <h5>Highly Professional Team</h5>
    <p>Mirationis ipsum dolor sit amet, consectetur adipiscing elit. Quid autem habent admiratio-nis, cum prope accesseris An hoc usque quaque, aliter in vita</p>
  </div>
  <div class="who" style="left:678px;top:340px">VERA CASTELL<span>Top Manager</span></div>
</section>

<!-- newsletter -->
<section class="section newsletter">
  <div class="abs mail-icon"><i></i><svg viewBox="0 0 20 16"><rect x="1" y="1" width="18" height="14"/><path d="M1 1l9 8 9-8"/></svg></div>
  <h6>News letter Signup</h6>
  <div class="abs nl-input">Enter Your Email</div>
  <div class="abs nl-btn">SUBSCRIBE</div>
</section>

<!-- gallery -->
<section class="section gallery">
  <h2 class="heading" style="top:75px"><svg style="fill:var(--green)"><use href="#paw"/></svg><span style="color:var(--brand)">Gallery</span></h2>
  <div class="rule" style="top:132px"></div>
  <div class="tile" style="left:139px;top:203px;background:linear-gradient(135deg,#6f8a3a,#c98a4c)" role="img" aria-label="Woman hugging a corgi outdoors"></div>
  <div class="tile" style="left:376px;top:203px;background:linear-gradient(180deg,#f4f4f4,#6a4b35)" role="img" aria-label="Brown puppy and tabby kitten on white"></div>
  <div class="tile" style="left:612px;top:203px;background:linear-gradient(135deg,#d9c7a8,#a88755)" role="img" aria-label="Couple with a golden retriever at home"></div>
  <div class="tile" style="left:847px;top:203px;background:linear-gradient(135deg,#7fa3c9,#e8d3b0)" role="img" aria-label="Vet holding a golden puppy"></div>
  <div class="tile" style="left:139px;top:426px;background:linear-gradient(135deg,#a5612e,#e3d6cc)" role="img" aria-label="Dog licking a smiling woman"></div>
  <div class="tile" style="left:376px;top:426px;background:linear-gradient(180deg,#f2f2f2,#c78b52)" role="img" aria-label="Girl holding kittens"></div>
  <div class="tile" style="left:612px;top:426px;background:linear-gradient(135deg,#dfe4e8,#4b4b4b)" role="img" aria-label="Dog and cat lying together"></div>
  <div class="tile" style="left:847px;top:426px;background:linear-gradient(135deg,#8fb0d4,#f0ece6)" role="img" aria-label="Vet and child with a white puppy"></div>
</section>

<!-- footer -->
<footer class="section footer">
  <h6 style="left:139px">QUICK LINK</h6>
  <ul style="left:143px"><li>Home</li><li>About</li><li>Services</li><li>gallery</li><li>Pricing</li><li>Faq</li><li>Contact US</li></ul>
  <h6 style="left:366px">CONTACT INFO</h6>
  <div class="col" style="left:369px"><p>2140 Willow Crest Lane,<br>Fairbanks,<br>Alaska 99701</p><p>369-555-0182<br>hello@velvetpaws.com<br>www.velvetpaws.com</p></div>
  <h6 style="left:629px">TIME HOURS</h6>
  <div class="col" style="left:629px"><p>M-F : 8am - 7pm<br>Sat : 8am - 5am<br>Sun : Noon - 5pm</p><p>Contact Us<br>For holiday hours</p></div>
  <h6 style="left:862px">NEWSLETTER</h6>
  <div class="f-input" style="top:121px">Your Name</div>
  <div class="f-input" style="top:165px">Your Email</div>
  <div class="f-btn">SIGN UP</div>
</footer>
<div class="section copy">Copyright 2022, velvetpaws, All Right Reserved</div>
</body>
</html>
```